UX/UI Design of mobile application for language learning through picture cards

We are looking for a Mobile Application Designer with knowledge of UX/UI concepts.

We best candidate is a skilled Mobile Application Designer with knowledge of last trends and with experience in completing similar tasks.

This is a test task. After successful completion, the best candidate will be given a full task.

```html
<!DOCTYPE html>
<html lang="en">
<head>
<meta charset="utf-8">
<title>Snap Lexicon – language cards</title>
<link href="https://fonts.googleapis.com/css2?family=Inter:wght@400;500;600&display=swap" rel="stylesheet">
<style>
:root{
  --canvas:#c9c9ee;
  --frame:#d7d6f6;
  --indigo:#5a55d9;
  --indigo-soft:#a29fe6;
  --chip:#b0aeea;
  --ink:#27275e;
  --white:#ffffff;
  --field:#6f6c9a;
  --night:#34326e;
}
*{margin:0;padding:0;box-sizing:border-box}
html,body{width:1200px;height:1164px;overflow:hidden}
body{background:var(--canvas);font-family:"Inter",sans-serif;position:relative}
.device{position:absolute;top:99px;width:466px;height:936px;border-radius:62px;background:var(--frame)}
.device--left{left:87px}
.device--right{left:650px}
.screen{position:absolute;left:16px;top:23px;width:433px;height:890px;border-radius:56px;overflow:hidden}
.screen--capture{background:var(--indigo)}
.brand{position:absolute;left:33px;top:48px;color:var(--white);font-weight:500;font-size:32px;line-height:34px;letter-spacing:-0.5px}
.panel{position:absolute;left:32px;top:139px;width:369px;height:711px;border-radius:30px;background:var(--indigo-soft)}
.photo{position:absolute;left:29px;top:25px;width:312px;height:406px;border-radius:18px;
  background:linear-gradient(180deg,#d9d2cb 0%,#ece8e3 40%,#c9a98a 70%,#8a5a36 100%)}
.highlight{position:absolute;left:3px;top:226px;width:154px;height:86px;border:1.5px dashed #ff6b5e;border-radius:6px;background:rgba(255,120,120,.25)}
.highlight span{position:absolute;right:8px;bottom:2px;color:var(--white);font-size:12px}
.question{position:absolute;left:0;right:0;top:449px;text-align:center;color:var(--ink);font-weight:500;font-size:16.5px}
.answer-field{position:absolute;left:86px;top:484px;width:198px;height:33px;border-radius:17px;background:var(--field);
  color:#a9a7cf;font-size:10px;font-style:italic;padding:11px 20px}
.confirm{position:absolute;left:300px;top:484px;width:33px;height:33px;border-radius:50%;background:var(--indigo);
  box-shadow:0 8px 14px rgba(70,60,200,.35);display:flex;align-items:center;justify-content:center}
.shutter{position:absolute;left:129px;top:545px;width:112px;height:112px;border-radius:50%;background:var(--indigo);
  box-shadow:0 10px 22px rgba(70,60,200,.35);display:flex;align-items:center;justify-content:center}
.shutter-label{position:absolute;left:0;right:0;top:681px;text-align:center;color:var(--white);font-size:14.5px}
.screen--quiz{background:radial-gradient(ellipse at 55% 55%,#6e6a8c 0%,#4a4784 45%,var(--night) 100%)}
.backdrop{position:absolute;inset:0}
.sheet{position:absolute;left:0;top:468px;width:433px;height:422px;background:var(--white);border-radius:115px 115px 0 0}
.flag{position:absolute;left:83px;top:60px;width:33px;height:33px;border-radius:50%;overflow:hidden;display:flex}
.flag i{flex:1}
.prompt{position:absolute;left:138px;top:66px;color:var(--ink);font-weight:600;font-size:16px}
.chip{position:absolute;height:32px;border-radius:16px;background:var(--chip);color:var(--white);font-size:12.5px;font-weight:500;
  display:flex;align-items:center;justify-content:center}
.chip--active{background:var(--indigo)}
.continue{position:absolute;left:254px;top:343px;width:147px;height:48px;border-radius:24px;background:var(--indigo);
  box-shadow:0 8px 18px rgba(70,60,200,.4);color:var(--white);font-size:13px;font-weight:500;padding-left:31px;display:flex;align-items:center}
.continue svg{position:absolute;right:12px;top:15px}
</style>
</head>
<body>
<div class="device device--left">
  <div class="screen screen--capture">
    <div class="brand">Snap<br>Lexicon</div>
    <div class="panel">
      <div class="photo" role="img" aria-label="Bright living room with a bed, tall windows, ceiling lamp and wooden floor">
        <div class="highlight"><span>Bed</span></div>
      </div>
      <p class="question">What is highlighted in the picture?</p>
      <div class="answer-field">Name the item</div>
      <div class="confirm"><svg width="16" height="12" viewBox="0 0 16 12"><path d="M1.5 6l4.5 4.5L14.5 1.5" fill="none" stroke="#fff" stroke-width="1.6" stroke-linecap="round" stroke-linejoin="round"/></svg></div>
      <div class="shutter"><svg width="38" height="38" viewBox="0 0 38 38"><path d="M19 3v32M3 19h32" stroke="#fff" stroke-width="5" stroke-linecap="round"/></svg></div>
      <p class="shutter-label">Take a Picture</p>
    </div>
  </div>
</div>

<div class="device device--right">
  <div class="screen screen--quiz">
    <div class="backdrop" role="img" aria-label="Blurred photo of the room behind the quiz"></div>
    <div class="sheet">
      <div class="flag"><i style="background:#0c4da2"></i><i style="background:#fff"></i><i style="background:#f0283e"></i></div>
      <p class="prompt">Find the correct word</p>
      <span class="chip chip--active" style="left:68px;top:122px;width:75px">Voodi</span>
      <span class="chip" style="left:156px;top:122px;width:52px">Lit</span>
      <span class="chip" style="left:221px;top:122px;width:62px">Seng</span>
      <span class="chip" style="left:296px;top:120px;width:75px">Sänky</span>
      <span class="chip" style="left:68px;top:171px;width:75px">Kama</span>
      <span class="chip" style="left:156px;top:171px;width:114px">Name the item</span>
      <div class="continue">Continue<svg width="18" height="16" viewBox="0 0 18 16"><path d="M1 8h15M9.5 1.5L16 8l-6.5 6.5" fill="none" stroke="#fff" stroke-width="2" stroke-linecap="round" stroke-linejoin="round"/></svg></div>
    </div>
  </div>
</div>
</body>
</html>
```